Create Brisk Lesson Studio a card design that will stick in the mind of prospects.

Brisk Lesson Studio specialises designs and produces training video, animation, illustration and text.

We need a card design that oozes class and leaves the prospect brimming with confidence.

The design will feature the Brisk Lesson Studio all black logo (uploaded). The design may also use the shade of orange from the orange version of the logo (uploaded). Note, just the color is to be used e.g. for the back of the card, not the orange logo itself.

The Brisk brand is about authenticity, quality, maturity and assurance. We are a safe buy when it comes to the prospects next project.

Target Market(s)

The primary target is training managers or others who are responsible for choosing to hire companies to produce their training media e.g. video. This will usually be a large spend so they need to have confidence.

Industry/Entity Type

Training

Contact Information for Business Card

FRONT:

Brisk Lesson Studio
Phone: 03 5172 4039
1st Floor, 418 Kellerby Road
Mt Ferncombe
VIC 3862
Australia
www.brisklesson.com.au

Lionel Petch
Founder and Lead Consultant
mobile: +61 3 0462 735 218
email: lionel@brisklesson.com.au

BACK:
Specialising in design and production of training:

video
animation
illustration
text

for delivery via internet, intranet and/or LMS.

Number of Pages Required

4 page

Font styles to use
Sans Serif

Requirements
Must have
• The black logo uploaded with the brief.
Nice to have
• The inclusion of the shade of orange found in the orange logo also uploaded with the brief. One example would be having the back of the card in this orange and using a white font for the text. But I want the designer to work this out.
Should not have
• No colours other than black and the orange included in the uploaded orange logo.

```html
<!DOCTYPE html>
<html lang="en">
<head>
<meta charset="utf-8">
<title>Brisk Lesson Studio – Business Card</title>
<link rel="stylesheet" href="https://fonts.googleapis.com/css2?family=Montserrat:wght@400;500;700&display=swap">
<style>
  :root {
    --bg: #2b2b2b;
    --card: #050505;
    --orange: #f2622a;
    --white: #ffffff;
    --muted: #d9d9d9;
    --rule: #555555;
  }
  * { box-sizing: border-box; margin: 0; padding: 0; }
  html, body {
    width: 1200px; height: 900px; overflow: hidden;
    background: var(--bg);
    font-family: "Montserrat", Arial, sans-serif;
    color: var(--white);
  }
  .canvas { position: relative; width: 1200px; height: 900px; }
  .card {
    position: absolute; left: 290px;
    width: 620px; height: 354px;
    background: var(--card);
    border-radius: 18px;
    box-shadow: 0 14px 30px rgba(0,0,0,.5);
  }
  .card--back { top: 71px; }
  .card--front { top: 475px; }

  .wordmark {
    position: absolute; display: flex; align-items: center; gap: 14px;
    font-weight: 700; line-height: 1.05;
  }
  .wordmark__dot {
    width: 26px; height: 26px; border-radius: 50%;
    flex: none;
  }
  .wordmark__name { font-size: 34px; }
  .card--back .wordmark { left: 48px; top: 122px; color: var(--orange); }
  .card--back .wordmark__dot { background: var(--orange); }
  .card--front .wordmark { left: 48px; top: 138px; color: var(--white); }
  .card--front .wordmark__dot { background: var(--white); }

  .services {
    position: absolute; left: 390px; top: 56px;
    list-style: none; font-size: 21px; font-weight: 400; line-height: 1.22;
  }
  .services li { display: flex; align-items: center; gap: 12px; }
  .services li::before {
    content: ""; width: 10px; height: 10px; border-radius: 50%;
    background: var(--orange);
  }
  .web {
    position: absolute; right: 140px; bottom: 52px;
    font-size: 18px; font-weight: 500;
  }
  .web__accent { color: var(--orange); }

  .divider {
    position: absolute; left: 322px; top: 60px; width: 1px; height: 234px;
    background: linear-gradient(var(--card), var(--rule) 30%, var(--rule) 70%, var(--card));
  }
  .details { position: absolute; left: 348px; top: 66px; }
  .details__name { font-size: 26px; font-weight: 700; color: var(--orange); }
  .details__role { font-size: 14px; margin-top: 2px; color: var(--muted); }
  .details__address { font-size: 14px; line-height: 1.3; margin-top: 12px; padding-left: 18px; color: var(--muted); }
  .contact { list-style: none; margin-top: 12px; font-size: 14px; line-height: 1.45; color: var(--muted); }
  .contact li { display: flex; align-items: center; gap: 8px; }
  .contact svg { width: 11px; height: 11px; flex: none; }
</style>
</head>
<body>
<main class="canvas">
  <section class="card card--back">
    <div class="wordmark">
      <span class="wordmark__dot"></span>
      <span class="wordmark__name">Brisk<br>Lesson<br>Studio</span>
    </div>
    <ul class="services">
      <li>Video</li>
      <li>Animation</li>
      <li>Illustration</li>
      <li>Text</li>
    </ul>
    <p class="web">www.<span class="web__accent">brisklesson</span>.com.au</p>
  </section>

  <section class="card card--front">
    <div class="wordmark">
      <span class="wordmark__dot"></span>
      <span class="wordmark__name">Brisk<br>Lesson<br>Studio</span>
    </div>
    <div class="divider"></div>
    <div class="details">
      <h1 class="details__name">Lionel Petch</h1>
      <p class="details__role">Founder and Lead Consultant</p>
      <p class="details__address">1st Floor, 418 Kellerby Road<br>Mt Ferncombe<br>VIC 3862</p>
      <ul class="contact">
        <li>
          <svg viewBox="0 0 12 12" aria-hidden="true"><path d="M2 1l2 0 1 3-1.3 1a6 6 0 0 0 3.3 3.3L8 7l3 1v2a1 1 0 0 1-1 1A9 9 0 0 1 1 2a1 1 0 0 1 1-1z" fill="var(--orange)"/></svg>
          03 5172 4039
        </li>
        <li>
          <svg viewBox="0 0 12 12" aria-hidden="true"><rect x="3" y="0.5" width="6" height="11" rx="1" fill="none" stroke="var(--orange)" stroke-width="1.2"/><circle cx="6" cy="9.5" r=".8" fill="var(--orange)"/></svg>
          +61 3 0462 735 218
        </li>
        <li>
          <svg viewBox="0 0 12 12" aria-hidden="true"><rect x="0.6" y="2" width="10.8" height="8" fill="none" stroke="var(--orange)" stroke-width="1.2"/><path d="M1 2.5l5 4 5-4" fill="none" stroke="var(--orange)" stroke-width="1.2"/></svg>
          lionel@brisklesson.com.au
        </li>
        <li>
          <svg viewBox="0 0 12 12" aria-hidden="true"><circle cx="6" cy="6" r="5.2" fill="none" stroke="var(--orange)" stroke-width="1.2"/><ellipse cx="6" cy="6" rx="2.3" ry="5.2" fill="none" stroke="var(--orange)" stroke-width="1"/><path d="M1 6h10" stroke="var(--orange)" stroke-width="1"/></svg>
          www.brisklesson.com.au
        </li>
      </ul>
    </div>
  </section>
</main>
</body>
</html>
```